Web Design Project

We are looking to for a redesign for www.valtemo.com. Valtemo Systems is a Managed Service Provider of IT solutions based is Calgary, Alberta, Canada. We are currently expanding into the Edmonton market and would like to lauch our new site with our expansion.
The design should be sleak in style and communicate a professional vision to our clients and prospects.

Thanks,
Owen

Target Market(s)

Small to medium size businesses looking to outsource or complement their IT solutions.

Industry/Entity Type

It Professional

```html
<!DOCTYPE html>
<html lang="en">
<head>
<meta charset="utf-8">
<title>Valtemo Systems – Managed IT Service Professionals</title>
<link href="https://fonts.googleapis.com/css2?family=Source+Sans+3:wght@400;600&display=swap" rel="stylesheet">
<style>
  :root {
    --sky-top: #a9dde9;
    --sky-mid: #d6eff7;
    --sky-low: #dff2f9;
    --bar-dark: #2b2b2b;
    --band-dark: #2e2f31;
    --teal-edge: #3fa6c2;
    --brand-top: #58c3d6;
    --brand-bottom: #2a9ab8;
    --ink: #141414;
    --white: #ffffff;
    --card-blue-a: #2680ad;
    --card-blue-b: #3aa5c8;
    --card-teal: #4cbdcd;
    --card-teal-b: #3fb0c6;
    --frame: #2a2a2a;
  }
  * { box-sizing: border-box; margin: 0; padding: 0; }
  html, body { width: 1200px; height: 798px; overflow: hidden; }
  body {
    position: relative;
    font-family: "Source Sans 3", "Myriad Pro", sans-serif;
    background: linear-gradient(to bottom, var(--sky-top) 0px, var(--sky-mid) 150px, var(--sky-low) 500px);
  }

  .top-bar {
    position: absolute; left: 0; top: 35px; width: 1200px; height: 45px;
    background: var(--bar-dark);
  }
  .brand {
    position: absolute; left: 138px; top: 0; width: 286px; height: 132px;
    border-radius: 0 0 14px 14px;
    background: linear-gradient(to bottom, var(--brand-top), var(--brand-bottom));
    display: flex; align-items: center; justify-content: center;
    padding-bottom: 8px;
  }
  .brand-name {
    color: var(--white); font-weight: 400; font-size: 48px; line-height: 1;
  }

  .main-nav {
    position: absolute; top: 35px; left: 528px; height: 45px;
    display: flex; align-items: center;
  }
  .main-nav a {
    color: var(--white); text-decoration: none; font-size: 26.5px; padding: 0 21px;
    border-left: 1px solid #7a7a7a; line-height: 28px;
  }
  .main-nav a:first-child { border-left: none; }

  .hero-copy { position: absolute; left: 94px; top: 248px; width: 540px; color: var(--ink); }
  .hero-copy h1 { font-weight: 400; font-size: 36px; line-height: 42px; margin-bottom: 4px; white-space: nowrap; }
  .hero-copy p { font-size: 17px; line-height: 22px; }
  .hero-copy p span { display: block; white-space: nowrap; }

  .hero-visual {
    position: absolute; left: 640px; top: 205px; width: 520px; height: 235px;
    background: linear-gradient(to bottom, #1c1c1e 0%, #2a2a2c 70%, rgba(200,230,240,0.4) 100%);
    border-radius: 2px;
  }

  .band-edge { position: absolute; left: 0; top: 505px; width: 1200px; height: 5px; background: var(--teal-edge); }
  .feature-band {
    position: absolute; left: 0; top: 510px; width: 1200px; height: 275px; background: var(--band-dark);
  }
  .footer-strip { position: absolute; left: 0; top: 785px; width: 1200px; height: 13px; background: var(--sky-top); }

  .card {
    position: absolute; top: 521px; width: 365px; height: 222px; color: var(--white);
  }
  .card h2 { position: absolute; left: 22px; top: 19px; font-weight: 400; font-size: 25px; line-height: 30px; white-space: nowrap; }
  .card p { position: absolute; font-size: 20px; line-height: 25px; }
  .card-spotlight { left: 24px; background: linear-gradient(to right, var(--card-blue-a), var(--card-blue-b)); }
  .card-partners { left: 416px; background: linear-gradient(to right, var(--card-teal-b), var(--card-teal)); }
  .card-support { left: 808px; background: linear-gradient(to right, var(--card-blue-b), var(--card-blue-a)); }

  .card-spotlight p { left: 38px; top: 61px; width: 170px; }
  .card-partners p { left: 36px; top: 61px; width: 170px; }
  .card-support p { left: 33px; top: 59px; width: 150px; }

  .card-image { position: absolute; border: 3px solid var(--frame); border-radius: 3px; }
  .card-spotlight .card-image {
    left: 204px; top: 55px; width: 150px; height: 113px;
    background: linear-gradient(135deg, #123048, #3a7fa3 50%, #1a3550);
  }
  .partner-badge {
    position: absolute; left: 210px; top: 57px; width: 136px; height: 80px;
    background: #1f1f1f; border-radius: 2px; box-shadow: 0 2px 4px rgba(0,0,0,0.4);
  }
  .card-support .card-image {
    left: 190px; top: 40px; width: 157px; height: 121px;
    background: linear-gradient(135deg, #c9ddea, #d9a884 55%, #8a5a3a);
  }
</style>
</head>
<body>
  <div class="top-bar"></div>
  <div class="brand">
    <span class="brand-name">Valtemo</span>
  </div>
  <nav class="main-nav">
    <a href="#">About Us</a>
    <a href="#">Solutions</a>
    <a href="#">Services</a>
    <a href="#">Contact Us</a>
  </nav>

  <section class="hero-copy">
    <h1>Managed IT Service Professionals</h1>
    <p>
      <span>Valtemo Systems employs an innovative managed service solution to</span>
      <span>provide our clients with technical expertise and superb customer</span>
      <span>service. Our goal is to ensure that our clients business requirements</span>
      <span>align with their technical needs in order to maximize their benefits</span>
    </p>
  </section>
  <div class="hero-visual" role="img" aria-label="Row of black server towers with a businessman leaning on them"></div>

  <div class="band-edge"></div>
  <div class="feature-band"></div>

  <article class="card card-spotlight">
    <h2>Spotlight</h2>
    <p>Keep your data secure and readily available with our online backup service</p>
    <div class="card-image" role="img" aria-label="Padlocks over a digital data background"></div>
  </article>

  <article class="card card-partners">
    <h2>Partners</h2>
    <p>We work with the best to bring you the best.</p>
    <div class="partner-badge" role="img" aria-label="Partner badge"></div>
  </article>

  <article class="card card-support">
    <h2>Live Support</h2>
    <p>Click here to access our Live support</p>
    <div class="card-image" role="img" aria-label="Support agent with headset"></div>
  </article>

  <div class="footer-strip"></div>
</body>
</html>
```